Ceate a flashy Car Cruise-In Flyer for Christian Car Club

Design a flyer for a Christian car club cruise-in at a local restaurant, Bramleys. Should include a car, truck and motorcycle. I'd like it to be striking and suitable for print and post on social media.

Pictures of a car, truck and motorcycle

Info to Include:
Every 3rd Sunday from April-October
Time: 1:30 pm
Location: Bramley's
4715 SE Alder Ln.
Murfreesboro

Website: Halvorn42.com

No preference in colors but should include and contrast with the included Halvorn logo. Also, examples of flyers are included of items I like. I would also like the vehicles to be later model so as not to scare people away that dont own classics. Maybe include an area that says: Exotic cars, Sports Cars, Muscle Cars, Torvas, Trucks and Motorcycles.

I am not sure what else to add to continue the project.

Target Market(s)

Christian car, truck and motorcycle enthusiasts

Industry/Entity Type

Automotive

Font styles to use
Serif

Requirements
Must have
• Pictures of a car, truck and motorcycle
• Info to Include:
• Every 3rd Sunday from April-October
• Time: 1:30 pm
• Location: Bramley's
• 4715 SE Alder Ln.
• Murfreesboro
• Website: Halvorn42.com
Nice to have
• All cars, trucks, and motorcycles welcome

```html
<!DOCTYPE html>
<html lang="en">
<head>
<meta charset="utf-8">
<title>Cruise In Flyer</title>
<link rel="stylesheet" href="https://fonts.googleapis.com/css2?family=Audiowide&family=Exo+2:wght@500;600;700&display=swap">
<style>
  :root {
    --bg: #d9d9d9;
    --paper: #ffffff;
    --red: #e3161f;
    --red-deep: #a8101a;
    --navy: #23305e;
    --maroon: #7a1520;
    --ink: #1a1a1a;
    --white: #ffffff;
  }
  * { margin: 0; padding: 0; box-sizing: border-box; }
  html, body { width: 1200px; height: 2250px; overflow: hidden; background: var(--bg); }
  .flyer {
    position: absolute; left: 40px; top: 335px;
    width: 1120px; height: 1579px;
    background: var(--paper); overflow: hidden;
    box-shadow: 8px 10px 24px rgba(0,0,0,.35);
    font-family: "Exo 2", sans-serif; color: var(--white);
  }
  .title {
    position: absolute; top: 50px; left: 0; width: 100%;
    text-align: center; font-family: "Audiowide", sans-serif;
    font-size: 132px; line-height: 1; letter-spacing: 2px;
    color: var(--red); -webkit-text-stroke: 4px var(--ink);
  }
  .categories {
    position: absolute; top: 202px; left: 0; width: 100%;
    display: flex; justify-content: center; gap: 22px;
    font-size: 25px; font-weight: 600; color: var(--red);
  }
  .categories span + span::before { content: "•"; color: var(--ink); margin-right: 22px; }
  .info-panel {
    position: absolute; left: 0; top: 820px; width: 100%; height: 759px;
    background: linear-gradient(115deg, var(--navy) 0%, #3b2350 45%, var(--maroon) 80%, #9b2a1e 100%);
  }
  .vehicle-photo {
    position: absolute; left: 0; top: 256px; width: 1120px; height: 660px;
    background: linear-gradient(180deg, #a9c0d6 0%, #6f8a6a 30%, #3d5232 55%, #585a5e 72%, #3b3c40 100%);
    clip-path: polygon(0 0, 100% 0, 100% 95%, 0 76%);
  }
  .bands { position: absolute; left: 0; top: 0; }
  .brand-name {
    position: absolute; top: 925px; left: 0; width: 1145px;
    text-align: center; font-size: 64px; font-weight: 700; letter-spacing: 4px;
    color: var(--white);
  }
  .schedule { position: absolute; left: 73px; top: 1060px; line-height: 1; font-weight: 600; }
  .schedule .day { font-size: 84px; }
  .schedule .season { font-size: 60px; margin-top: 18px; }
  .schedule .time { font-size: 88px; margin-top: 14px; }
  .location-bar {
    position: absolute; left: 0; top: 1335px; width: 100%; height: 87px;
    background: var(--red); display: flex; align-items: center; gap: 20px;
    padding-left: 76px; font-size: 44px; font-weight: 600;
  }
  .welcome {
    position: absolute; top: 1444px; left: 0; width: 1120px;
    text-align: center; font-size: 32px; font-weight: 500;
  }
  .website {
    position: absolute; left: 230px; top: 1498px; width: 660px; height: 81px;
    background: var(--red); display: flex; align-items: center; justify-content: center;
    font-size: 42px; font-weight: 600;
  }
</style>
</head>
<body>
  <main class="flyer">
    <div class="info-panel"></div>
    <div class="vehicle-photo" role="img" aria-label="Photo of a white late-model sports car parked on a road with trees behind"></div>
    <svg class="bands" width="1120" height="1579" viewBox="0 0 1120 1579" aria-hidden="true">
      <polygon points="0,250 1120,250 1120,372 0,264" fill="var(--red)"/>
      <polygon points="280,282 1120,300 1120,372" fill="var(--red-deep)"/>
      <polygon points="0,756 1120,890 1120,940 0,845" fill="var(--red)"/>
      <polygon points="0,800 1120,905 1120,940 0,845" fill="var(--red-deep)"/>
    </svg>

    <h1 class="title">CRUISE IN</h1>
    <p class="categories">
      <span>Exotic cars</span><span>Sports Cars</span><span>Muscle Cars</span><span>Torvas</span><span>Trucks</span><span>Motorcycles.</span>
    </p>

    <div class="brand-name">HALVORN</div>

    <div class="schedule">
      <p class="day">Every 3rd Sunday</p>
      <p class="season">From April-October</p>
      <p class="time">1:30 pm</p>
    </div>

    <div class="location-bar">
      <svg width="34" height="44" viewBox="0 0 34 44" aria-hidden="true">
        <path d="M17 2C9 2 3 8 3 16c0 10 14 24 14 24s14-14 14-24C31 8 25 2 17 2z" fill="none" stroke="var(--white)" stroke-width="3"/>
        <circle cx="17" cy="16" r="5" fill="none" stroke="var(--white)" stroke-width="3"/>
      </svg>
      <span>Bramley's 4715 SE Alder Ln. Murfreesboro</span>
    </div>

    <p class="welcome">All cars, trucks and motorcycles welcome</p>
    <div class="website">Halvorn42.com</div>
  </main>
</body>
</html>
```